Verdant Loop Advisors, LLC

I am looking for a simple, clear layout with my logo prominent and embossed, on the best quality card stock available. I would like the business name and phone number included on the card as well......I dont want my name anywhere on the card and I would like my logo embossed on the card......something simple with a white back......open to designs as long as they go along with recycling symbols and green type stuff.....The address, website, cell number, fax number, and email are listed below

5374 Tillbury Fenwood Road
Brackenridge, MD 20911

c. 240.555.0143 f. 240.555.0187
e. sales@verdantloopadvisors.example
w. www.verdantloopadvisors.example

Industry/Entity Type

Recycling

```html
<!DOCTYPE html>
<html lang="en">
<head>
<meta charset="utf-8">
<title>Verdant Loop Advisors, LLC — Business Card</title>
<link rel="stylesheet" href="https://fonts.googleapis.com/css2?family=Arimo:wght@400;700&display=swap">
<style>
  :root {
    --canvas-bg: #ecede0;
    --card-white: #fbfbf8;
    --panel-stone: #dcddd2;
    --brand-green: #1f7a3c;
    --ink: #1b1b1b;
    --ink-soft: #2a2a2a;
  }
  * { box-sizing: border-box; margin: 0; padding: 0; }
  html, body {
    width: 1200px;
    height: 768px;
    overflow: hidden;
    background: var(--canvas-bg);
  }
  .canvas {
    position: relative;
    width: 1200px;
    height: 768px;
  }
  .business-card {
    position: absolute;
    left: 250px;
    top: 168px;
    width: 700px;
    height: 432px;
    background: var(--card-white);
    box-shadow: 0 3px 10px rgba(0, 0, 0, 0.22);
    display: flex;
    font-family: "Arimo", Arial, sans-serif;
  }
  .brand-panel {
    width: 210px;
    height: 100%;
    background: radial-gradient(circle at 40% 35%, #e3e4da 0%, var(--panel-stone) 100%);
    position: relative;
  }
  .brand-mark {
    position: absolute;
    left: 38px;
    top: 106px;
    width: 130px;
    height: 130px;
    border-radius: 50%;
    background: var(--brand-green);
  }
  .card-content {
    flex: 1;
    padding: 66px 20px 0 25px;
    color: var(--ink);
  }
  .company-name {
    font-weight: 700;
    font-size: 38px;
    line-height: 1.05;
    letter-spacing: 1.5px;
    text-transform: uppercase;
    color: var(--ink);
  }
  .address,
  .contact {
    font-style: normal;
    font-weight: 400;
    font-size: 24px;
    line-height: 35px;
    letter-spacing: 0.8px;
    color: var(--ink-soft);
    white-space: nowrap;
  }
  .address { margin-top: 70px; }
  .contact { margin-top: 27px; }
  .contact-line { display: block; }
  .phone-line { position: relative; }
  .phone-icon {
    position: absolute;
    left: -22px;
    top: 8px;
    width: 14px;
    height: 18px;
  }
</style>
</head>
<body>
<main class="canvas">
  <article class="business-card" aria-label="Business card for Verdant Loop Advisors, LLC">
    <div class="brand-panel">
      <span class="brand-mark" aria-hidden="true"></span>
    </div>
    <div class="card-content">
      <h1 class="company-name">Verdant Loop<br>Advisors LLC</h1>
      <address class="address">
        5374 Tillbury Fenwood Road<br>
        Brackenridge, MD 20911
      </address>
      <p class="contact">
        <span class="contact-line phone-line">
          <svg class="phone-icon" viewBox="0 0 14 18" aria-hidden="true">
            <path d="M4 1 C2 1 1 3 1 6 C1 11 4 16 8 17 C10 17.5 11 16.5 12 15 L9.5 12 L7.5 13 C6 12 4.5 9 4.5 7 L6.5 6 L5.5 1.5 Z" fill="var(--brand-green)"/>
          </svg>
          240.555.0143 | 240.555.0187
        </span>
        <span class="contact-line">sales@verdantloopadvisors.example</span>
        <span class="contact-line">www.verdantloopadvisors.example</span>
      </p>
    </div>
  </article>
</main>
</body>
</html>
```